Stationery and Business Card Design

We need stationary design for our new company pelvanta. Pelvanta is a company that provides city apartment rentals for tourists in Athens We need business cards, letterheads for A4 and A5 and envelopes for A4 A5. The design needs to be modern, friendly and corporate.

Target Market(s)

City Tourists

Industry/Entity Type

Tourism

```html
<!DOCTYPE html>
<html lang="en">
<head>
<meta charset="utf-8">
<title>Pelvanta Stationery</title>
<link rel="stylesheet" href="https://fonts.googleapis.com/css2?family=Open+Sans:wght@400;600&family=Quicksand:wght@400;500&display=swap">
<style>
  :root {
    --brand: #820a7c;
    --ink: #2e3136;
    --paper: #ffffff;
    --backdrop: #efefef;
    --muted: #7a2a76;
  }
  * { box-sizing: border-box; margin: 0; padding: 0; }
  html, body { width: 1200px; height: 1000px; overflow: hidden; }
  body {
    background: var(--backdrop);
    position: relative;
    font-family: "Open Sans", Arial, sans-serif;
    color: var(--ink);
  }
  .sheet { position: absolute; background: var(--paper); box-shadow: 0 2px 8px rgba(0,0,0,.18); }

  .brand-lockup { display: flex; align-items: center; gap: 10px; color: var(--brand); font-weight: 600; }
  .brand-lockup .mark { background: var(--brand); flex: none; }

  /* Letterhead */
  .letterhead { left: 130px; top: 40px; width: 430px; height: 608px; }
  .letterhead .brand-lockup { position: absolute; left: 40px; top: 36px; font-size: 24px; }
  .letterhead .mark { width: 26px; height: 26px; }
  .contact-list { position: absolute; left: 40px; bottom: 100px; list-style: none;
    font-family: "Quicksand", Arial, sans-serif; font-size: 9px; color: var(--brand); }
  .contact-list li { display: flex; align-items: center; gap: 8px; margin-top: 6px; }
  .contact-list svg { width: 12px; height: 12px; }
  .footer-band { position: absolute; left: 0; right: 0; bottom: 0; height: 76px; background: var(--brand);
    display: flex; align-items: center; justify-content: center; }
  .footer-band .name { color: var(--paper); font-size: 22px; font-weight: 400;
    border-bottom: 1px solid rgba(255,255,255,.6); padding: 0 14px 4px; }

  /* Envelope */
  .envelope { left: 650px; top: 40px; width: 430px; height: 590px; border-radius: 22px 22px 0 0; overflow: hidden; }
  .envelope .flap { position: absolute; left: 0; right: 0; top: 0; height: 100px; background: var(--brand); }
  .envelope .brand-lockup { position: absolute; left: 40px; top: 136px; font-size: 24px; }
  .envelope .mark { width: 26px; height: 26px; }
  .envelope .footer-band { height: 60px; }

  /* Business cards */
  .card { width: 370px; height: 214px; top: 712px; }
  .card-front { left: 100px; border: 14px solid var(--brand); display: flex; align-items: center; justify-content: center; }
  .card-front .brand-lockup { font-size: 46px; gap: 16px; }
  .card-front .mark { width: 42px; height: 42px; }

  .card-back { left: 610px; overflow: hidden; }
  .card-back .chevron { position: absolute; inset: 0; }
  .card-back .brand-lockup { position: absolute; left: 18px; top: 90px; font-size: 24px; gap: 8px; }
  .card-back .mark { width: 18px; height: 18px; }
  .holder { position: absolute; right: 22px; top: 34px; text-align: right; color: var(--paper);
    font-family: "Quicksand", Arial, sans-serif; }
  .holder .person { font-size: 16px; letter-spacing: .5px; }
  .holder .role { font-size: 13px; opacity: .85; }
  .card-back .contact-list { left: auto; right: 22px; bottom: 14px; color: var(--paper); font-size: 10px; }
  .card-back .contact-list li { justify-content: flex-end; margin-top: 8px; }
</style>
</head>
<body>

<svg width="0" height="0" style="position:absolute" aria-hidden="true">
  <defs>
    <symbol id="icon-phone" viewBox="0 0 12 12"><circle cx="6" cy="6" r="5.4" fill="none" stroke="currentColor"/><rect x="4.2" y="3" width="3.6" height="6" rx=".6" fill="none" stroke="currentColor" stroke-width=".8"/></symbol>
    <symbol id="icon-mail" viewBox="0 0 12 12"><circle cx="6" cy="6" r="5.4" fill="none" stroke="currentColor"/><rect x="3.3" y="4.2" width="5.4" height="3.6" fill="none" stroke="currentColor" stroke-width=".8"/><path d="M3.3 4.2 6 6.3 8.7 4.2" fill="none" stroke="currentColor" stroke-width=".8"/></symbol>
    <symbol id="icon-web" viewBox="0 0 12 12"><circle cx="6" cy="6" r="5.4" fill="none" stroke="currentColor"/><circle cx="6" cy="6" r="2.8" fill="none" stroke="currentColor" stroke-width=".8"/><path d="M3.2 6h5.6M6 3.2v5.6" stroke="currentColor" stroke-width=".6"/></symbol>
    <symbol id="icon-home" viewBox="0 0 12 12"><circle cx="6" cy="6" r="5.4" fill="none" stroke="currentColor"/><path d="M3.4 6.2 6 3.6l2.6 2.6V8.6H3.4z" fill="currentColor"/></symbol>
  </defs>
</svg>

<section class="sheet letterhead" aria-label="Letterhead">
  <div class="brand-lockup"><span class="mark"></span>Pelvanta</div>
  <ul class="contact-list">
    <li><svg><use href="#icon-phone"/></svg>000-0000-000</li>
    <li><svg><use href="#icon-mail"/></svg>hello@pelvanta-mail.com</li>
    <li><svg><use href="#icon-web"/></svg>www.pelvanta.com</li>
  </ul>
  <div class="footer-band"><span class="name">Pelvanta</span></div>
</section>

<section class="sheet envelope" aria-label="Envelope">
  <div class="flap"></div>
  <div class="brand-lockup"><span class="mark"></span>Pelvanta</div>
  <div class="footer-band"><span class="name">Pelvanta</span></div>
</section>

<section class="sheet card card-front" aria-label="Business card front">
  <div class="brand-lockup"><span class="mark"></span>Pelvanta</div>
</section>

<section class="sheet card card-back" aria-label="Business card back">
  <svg class="chevron" viewBox="0 0 370 214" preserveAspectRatio="none" aria-hidden="true">
    <polygon points="142,0 370,0 370,214 142,214 190,107" fill="var(--brand)"/>
    <polygon points="122,0 132,0 180,107 132,214 122,214 170,107" fill="var(--brand)"/>
  </svg>
  <div class="brand-lockup"><span class="mark"></span>Pelvanta</div>
  <div class="holder">
    <p class="person">YOUR NAME</p>
    <p class="role">Your Position</p>
  </div>
  <ul class="contact-list">
    <li>000-0000-000<svg><use href="#icon-phone"/></svg></li>
    <li>hello@pelvanta-mail.com<svg><use href="#icon-mail"/></svg></li>
    <li>www.pelvanta.com<svg><use href="#icon-web"/></svg></li>
    <li>Your Address<svg><use href="#icon-home"/></svg></li>
  </ul>
</section>

</body>
</html>
```